Helix Anchor Works Website

Hello we are a screw piling business based in Sydney.
Screw piling is basically drilling steel into the ground with a excavator.

The website needs to have similar information as http://www.brightgroundworks.com.au/. It is basically the same business.

The business name is Helix Anchor Works.

Logo is attached.

Website needs to be wordpress ready.
With SEO.
Want to be able to edit in wordpress.

Target Market(s)

Business to Business and Normal

Industry/Entity Type

Construction

Coding

Coded - Design and coding required

Number of Pages Required

5+ page

Font styles to use
Serif
Sans Serif
Decorative

Requirements
Nice to have
• Information about screw piering.

```html
<!DOCTYPE html>
<html lang="en">
<head>
<meta charset="utf-8">
<title>Helix Anchor Works</title>
<link href="https://fonts.googleapis.com/css2?family=Raleway:wght@400;500;600;700&family=Tinos:wght@700&display=swap" rel="stylesheet">
<style>
:root{
  --blue:#1f6fd6;
  --blue-top:#2f80d8;
  --blue-dark:#1558c4;
  --ink:#1d1d1d;
  --muted:#555;
  --grey-band:#ececec;
  --footer:#3a3a3a;
  --footer-text:#e4e4e4;
  --white:#fff;
}
*{box-sizing:border-box;margin:0;padding:0}
html,body{width:1200px;height:2190px;overflow:hidden}
body{font-family:"Raleway",sans-serif;color:var(--ink);background:var(--white);position:relative}
.abs{position:absolute}
/* top bar */
.topbar{left:0;top:0;width:1200px;height:36px;background:var(--blue-top)}
.topbar .social{right:88px;top:6px;display:flex;gap:8px}
.dot-icon{width:24px;height:24px;border-radius:50%;background:rgba(255,255,255,.22);border:1px solid rgba(255,255,255,.35)}
/* header */
.header{left:0;top:36px;width:1200px;height:92px;background:var(--white)}
.brand{left:88px;top:30px;font-size:27px;font-weight:700;color:var(--blue);letter-spacing:.3px;display:flex;align-items:center;gap:10px}
.brand .mark{width:22px;height:22px;background:var(--blue)}
.nav{right:86px;top:40px;display:flex;gap:8px;font-size:16px}
.nav a{color:var(--ink);text-decoration:none;padding:5px 15px;border-radius:3px}
.nav a.active{background:var(--blue-top);color:var(--white)}
/* hero */
.hero{left:0;top:128px;width:1200px;height:482px;background:linear-gradient(100deg,#6f7b86 0%,#a3acb5 35%,#c9ced3 60%,#8e969d 100%)}
.hero-title{left:669px;top:299px;width:445px;height:57px;background:rgba(30,30,30,.82);color:#fff;font-size:25px;font-weight:500;display:flex;align-items:center;padding-left:38px;letter-spacing:.3px;clip-path:polygon(14px 0,100% 0,100% 100%,0 100%)}
.hero-sub{left:602px;top:375px;width:512px;height:59px;background:rgba(30,30,30,.72);color:#eee;font-size:14px;line-height:23px;padding:7px 20px 0 32px;clip-path:polygon(14px 0,100% 0,100% 100%,0 100%)}
.hero-arrow{top:373px;width:26px;height:26px;border:2px solid #fff;border-radius:50%}
.hero-dots{left:552px;top:584px;display:flex;gap:24px}
.hero-dots span{width:11px;height:11px;border-radius:50%;background:#333;border:2px solid #888}
.hero-dots span.on{background:var(--blue);border-color:#fff}
/* services */
.section-title{width:1200px;text-align:center;font-size:37px;font-weight:700}
.section-title em{font-style:normal;color:var(--blue)}
.section-sub{width:1200px;text-align:center;font-size:12px;color:#777}
.card{top:739px;width:308px;height:338px;background:#f6f6f6;box-shadow:0 12px 10px -8px rgba(0,0,0,.25)}
.card .photo{width:308px;height:154px}
.card h3{font-size:17px;font-weight:500;color:var(--blue);margin:20px 0 0 20px}
.card p{font-size:12.5px;line-height:22px;color:#444;margin:9px 18px 0 20px}
.btn{display:inline-block;margin:14px 0 0 20px;background:var(--blue);color:#fff;font-size:12px;padding:8px 13px;border-radius:2px}
/* advantages / gallery band */
.band{left:0;top:1118px;width:1200px;height:386px;background:var(--grey-band)}
.serif-head{font-family:"Tinos",serif;font-size:24px;font-weight:700}
.serif-head em{font-style:normal;color:var(--blue)}
.rule{height:4px;width:166px;background:linear-gradient(90deg,var(--blue) 0 66px,#aaa 66px)}
.adv{left:86px;width:440px;display:flex;gap:30px}
.adv svg{flex:none}
.adv h4{font-size:12.5px;font-weight:600;letter-spacing:.2px;margin-bottom:6px}
.adv p{font-size:12.5px;line-height:23px;color:#444}
.thumb{width:156px;height:103px}
/* testimonial */
.quote{left:0;top:1504px;width:1200px;height:200px;background:linear-gradient(180deg,#252525,#1a1a1a)}
.quote p{left:200px;top:34px;width:800px;text-align:center;color:#f0f0f0;font-size:15.5px;line-height:29px}
.quote .name{left:0;top:124px;width:1200px;text-align:center;color:#fff;font-size:18px}
.qdots{left:568px;top:167px;display:flex;gap:14px}
.qdots span{width:12px;height:12px;border-radius:50%;border:1.5px solid #ddd}
.qdots span.on{background:#fff}
/* partners */
.partners{left:0;top:1704px;width:1200px;height:172px}
.badge{top:44px;width:96px;height:96px;border-radius:50%;border:3px solid #bbb;background:#f3f3f3}
/* footer */
.footer{left:0;top:1876px;width:1200px;height:266px;background:var(--footer);color:var(--footer-text)}
.footer h5{font-size:19px;font-weight:500;letter-spacing:.3px;color:#fff}
.footer p,.footer li{font-size:13px;line-height:21px}
.footer ul{list-style:none}
.footer li{margin-bottom:9px}
.fbrand{left:88px;top:44px;font-size:22px;font-weight:700;color:#fff}
.contact-row{display:flex;gap:16px;align-items:flex-start;margin-top:10px}
.newsletter{left:870px;top:122px;width:244px;height:40px;border-radius:20px;background:#2a2a2a}
.send{right:0;top:0;width:72px;height:40px;border-radius:20px;background:var(--blue);color:#fff;font-size:13px;display:flex;align-items:center;justify-content:center}
.fsocial{left:872px;top:180px;display:flex;gap:22px}
.fsocial span{width:30px;height:30px;border-radius:50%;border:1.5px solid #ddd}
.copyright{left:0;top:2142px;width:1200px;height:48px;background:var(--blue-dark);color:#e8eefb;font-size:13px;display:flex;align-items:center;justify-content:center}
</style>
</head>
<body>

<div class="abs topbar">
  <div class="abs social"><span class="dot-icon"></span><span class="dot-icon"></span><span class="dot-icon"></span><span class="dot-icon"></span></div>
</div>

<header class="abs header">
  <div class="abs brand"><span class="mark"></span>Helix Anchor Works</div>
  <nav class="abs nav">
    <a class="active">Home</a><a>About us</a><a>Products</a><a>Benefits</a><a>FAQ</a><a>Contact us</a>
  </nav>
</header>

<section class="abs hero" role="img" aria-label="Worker in hi-vis gear driving a screw pile with a power tool beside steel posts"></section>
<div class="abs hero-title">WELCOME TO HELIX ANCHOR WORKS</div>
<div class="abs hero-sub">Excepteur sint occaecat cupidatat non proident, sunt in culpa qui officia deserunt mollit anim id est laborum</div>
<svg class="abs hero-arrow" style="left:20px" viewBox="0 0 26 26"><path d="M15 8l-5 5 5 5" fill="none" stroke="#fff" stroke-width="2"/></svg>
<svg class="abs hero-arrow" style="left:1158px" viewBox="0 0 26 26"><path d="M11 8l5 5-5 5" fill="none" stroke="#fff" stroke-width="2"/></svg>
<div class="abs hero-dots"><span class="on"></span><span></span><span></span></div>

<h2 class="abs section-title" style="left:0;top:640px">Our <em>Services</em></h2>
<p class="abs section-sub" style="left:0;top:692px">proin at ante sed quam malesuada rutrum non ut orci. Aenean ullamcorper placerat erat</p>

<article class="abs card" style="left:86px">
  <div class="photo" role="img" aria-label="Technician working with hoses and fittings in a workshop" style="background:linear-gradient(120deg,#6a7480,#b0a28e,#d1803c)"></div>
  <h3>Domestic Screw Pillers</h3>
  <p>Excepteur sint occaecat cupidatat non proident, sunt in culpa qui officia deserunt mollit anim id est laborum enim ipsam voluptatem.</p>
  <span class="btn">Read More</span>
</article>
<article class="abs card" style="left:448px">
  <div class="photo" role="img" aria-label="Container yard with stacked shipping containers and cranes" style="background:linear-gradient(180deg,#9fb4c8,#c48a52 55%,#4c6a8a)"></div>
  <h3>Commercial Screw Pillers</h3>
  <p>Excepteur sint occaecat cupidatat non proident, sunt in culpa qui officia deserunt mollit anim id est laborum enim ipsam voluptatem.</p>
  <span class="btn">Read More</span>
</article>
<article class="abs card" style="left:806px">
  <div class="photo" role="img" aria-label="Construction worker in hard hat crouching under a cloudy sky" style="background:linear-gradient(180deg,#9ec3e0,#dce9f2 60%,#6f8f5a)"></div>
  <h3>Demountable Screw Pillers</h3>
  <p>Excepteur sint occaecat cupidatat non proident, sunt in culpa qui officia deserunt mollit anim id est laborum enim ipsam voluptatem.</p>
  <span class="btn">Read More</span>
</article>

<section class="abs band">
  <h2 class="abs serif-head" style="left:88px;top:32px">Our <em>Advantages</em></h2>
  <div class="abs rule" style="left:86px;top:70px"></div>
  <h2 class="abs serif-head" style="left:606px;top:32px">Our <em>Gallery</em></h2>
  <div class="abs rule" style="left:604px;top:70px"></div>

  <div class="abs adv" style="top:113px">
    <svg width="40" height="40" viewBox="0 0 40 40"><circle cx="20" cy="20" r="18" fill="var(--blue)"/><circle cx="20" cy="20" r="12" fill="none" stroke="#fff" stroke-width="2"/><path d="M20 20l6-6" stroke="#fff" stroke-width="2.5"/></svg>
    <div><h4>SPEED OF INSTALLATION</h4><p>Lorem ipsum dolor sit ame sectetur adipsing elit. Praesentall est quilrs turpis posuere sodales.</p></div>
  </div>
  <div class="abs adv" style="top:195px">
    <svg width="40" height="40" viewBox="0 0 40 40"><circle cx="20" cy="20" r="18" fill="#555"/><circle cx="20" cy="20" r="13" fill="none" stroke="#fff" stroke-width="2"/><path d="M24 14h-6a3 3 0 0 0 0 6h4a3 3 0 0 1 0 6h-6M20 11v18" fill="none" stroke="#fff" stroke-width="2"/></svg>
    <div><h4>CONTROL FOUNDATION COSTS</h4><p>Lorem ipsum dolor sit ame sectetur adipsing elit. Praesentall est quilrs turpis posuere sodales.</p></div>
  </div>
  <div class="abs adv" style="top:277px">
    <svg width="40" height="40" viewBox="0 0 40 40"><path d="M34 20A14 14 0 1 1 20 6" fill="none" stroke="#555" stroke-width="2.5" stroke-dasharray="4 0"/><path d="M20 12v9l6 4" fill="none" stroke="#555" stroke-width="2.5"/></svg>
    <div><h4>SHORT LEAD-TIMES</h4><p>Lorem ipsum dolor sit ame sectetur adipsing elit. Praesentall est quilrs turpis posuere sodales.</p></div>
  </div>

  <div class="abs thumb" style="left:604px;top:111px;background:linear-gradient(135deg,#6d8fb8,#c9ccd0)" role="img" aria-label="Large industrial pipe fitting"></div>
  <div class="abs thumb" style="left:781px;top:111px;background:linear-gradient(135deg,#c86a4a,#2a74c2)" role="img" aria-label="Blue pipework in a plant room"></div>
  <div class="abs thumb" style="left:957px;top:111px;background:linear-gradient(135deg,#8d8f92,#e4e5e7)" role="img" aria-label="Rows of machined steel fittings"></div>
  <div class="abs thumb" style="left:604px;top:240px;background:linear-gradient(135deg,#3a85c4,#c7a58c)" role="img" aria-label="Worker operating machinery"></div>
  <div class="abs thumb" style="left:781px;top:240px;background:linear-gradient(135deg,#2d2d2f,#9a9ca0)" role="img" aria-label="Close view of a steel flange"></div>
  <div class="abs thumb" style="left:957px;top:240px;background:linear-gradient(135deg,#2f6f4a,#2c5fa8)" role="img" aria-label="Engineers inspecting equipment"></div>
</section>

<section class="abs quote">
  <svg class="abs" style="left:155px;top:22px" width="28" height="22" viewBox="0 0 28 22"><path d="M2 2h10v10l-4 8H4l3-8H2zM16 2h10v10l-4 8h-4l3-8h-5z" fill="#fff"/></svg>
  <p class="abs">Nam eu eleifend nulla. Duis consectetur sit amet risus sit amet venenatis. Pellentesque pulvinar ante a tincidunt placerat. Donec dapibus efficitur arcu, a rhoncus lectus egestas elementum.</p>
  <svg class="abs" style="left:1022px;top:72px" width="28" height="22" viewBox="0 0 28 22"><path d="M26 20H16V10l4-8h4l-3 8h5zM12 20H2V10l4-8h4l-3 8h5z" fill="#fff"/></svg>
  <div class="abs name">Sam Harlow</div>
  <div class="abs qdots"><span></span><span></span><span class="on"></span></div>
</section>

<section class="abs partners">
  <svg class="abs" style="left:86px;top:74px" width="18" height="26" viewBox="0 0 18 26"><path d="M14 3L5 13l9 10" fill="none" stroke="#222" stroke-width="3"/></svg>
  <div class="abs badge" style="left:161px"></div>
  <div class="abs badge" style="left:356px"></div>
  <div class="abs badge" style="left:548px"></div>
  <div class="abs badge" style="left:740px"></div>
  <div class="abs badge" style="left:935px"></div>
  <svg class="abs" style="left:1094px;top:74px" width="18" height="26" viewBox="0 0 18 26"><path d="M4 3l9 10-9 10" fill="none" stroke="#222" stroke-width="3"/></svg>
</section>

<footer class="abs footer">
  <div class="abs fbrand">Helix Anchor Works</div>
  <p class="abs" style="left:88px;top:102px;width:222px">Nemo enim ipsam voluptatem quia voluptas sit aspernatur aut odit aut fugit, sed quia consequuntur magni dolores eos qui ratione.</p>

  <div class="abs" style="left:377px;top:42px;width:220px">
    <h5>CONTACT US</h5>
    <p style="margin-top:14px">Neque porro quisquam est, qui dolore ipsum quia dolor sit</p>
    <div class="contact-row" style="margin-top:16px"><svg width="12" height="16" viewBox="0 0 12 16"><path d="M6 1a5 5 0 0 1 5 5c0 4-5 9-5 9S1 10 1 6a5 5 0 0 1 5-5z" fill="#fff"/><circle cx="6" cy="6" r="2" fill="var(--footer)"/></svg><p>No: 14 B, Coppervale Rd<br>Marlow Park, NSW, AU</p></div>
    <div class="contact-row"><svg width="12" height="14" viewBox="0 0 12 14"><path d="M2 1l3 3-1.5 2a8 8 0 0 0 3.5 3.5L9 8l3 3-2 2C5 12 1 7 0 3z" fill="#fff"/></svg><p>+1800 555 207</p></div>
    <div class="contact-row"><svg width="14" height="12" viewBox="0 0 14 12"><rect x="0" y="1" width="14" height="10" fill="#fff"/><path d="M0 1l7 5 7-5" fill="none" stroke="var(--footer)" stroke-width="1.3"/></svg><p>hello@helixanchor.example</p></div>
  </div>

  <div class="abs" style="left:637px;top:42px">
    <h5>QUICK LINKS</h5>
    <ul style="margin-top:16px"><li>About us</li><li>Products</li><li>Benefits</li><li>FAQ</li><li>Contact us</li></ul>
  </div>

  <div class="abs" style="left:870px;top:42px;width:250px">
    <h5>NEWSLETTER</h5>
    <p style="margin-top:10px">Neque porro quisquam est, qui dolorem ipsum quia dolor sit amet.</p>
  </div>
  <div class="abs newsletter"><div class="abs send">SEND</div></div>
  <div class="abs fsocial"><span></span><span></span><span></span><span></span></div>
</footer>

<div class="abs copyright">© 2015 Helix Anchor Works. All Rights Reserved</div>

</body>
</html>
```